Rocket business card

Modern business card design, use of color is good with clean space too.

Things to include on card:

Quote: I add fuel to your optometry practice

- Eyewear Sales
- Admin Duties
- Revenue Collection
- Leadership
- Tech Adoption
- COGS Reduction
- Product Sourcing
-Medical Growth

Dalton Vessey, CEO
Glint Harbor
Text Me! 847-302-1964
dalton@glintharbor.example

```html
<!DOCTYPE html>
<html lang="en">
<head>
<meta charset="utf-8">
<title>Glint Harbor – Business Card</title>
<link href="https://fonts.googleapis.com/css2?family=Roboto:wght@400;500;700&display=swap" rel="stylesheet">
<style>
  :root {
    --stage: #e6e6e6;
    --card-black: #0b0b0b;
    --ink-white: #f4f4f4;
    --ink-muted: #d6d6d6;
    --accent-orange: #f39a22;
    --accent-red: #e0353a;
    --accent-deep: #ea5a2c;
  }
  * { box-sizing: border-box; margin: 0; padding: 0; }
  html, body {
    width: 1200px; height: 912px; overflow: hidden;
    background: var(--stage);
    font-family: "Roboto", Arial, sans-serif;
  }
  .sheet { position: relative; width: 1200px; height: 912px; }
  .card {
    position: absolute; left: 250px; width: 700px; height: 400px;
    background: var(--card-black);
    color: var(--ink-white);
    overflow: hidden;
    box-shadow: 0 10px 24px rgba(0,0,0,0.25);
  }
  .card--back { top: 40px; }
  .card--front { top: 472px; }

  /* wordmark */
  .wordmark {
    position: absolute;
    display: flex; flex-direction: column; align-items: center; gap: 14px;
  }
  .wordmark__dot {
    width: 52px; height: 52px; border-radius: 50%;
    background: var(--accent-orange);
  }
  .wordmark__name {
    font-weight: 500; font-size: 40px; letter-spacing: 1px;
    color: var(--ink-white); line-height: 1; white-space: nowrap;
  }
  .card--back .wordmark { left: 300px; top: 62px; width: 330px; }
  .card--front .wordmark { left: 370px; top: 52px; width: 270px; }
  .card--front .wordmark__dot { width: 42px; height: 42px; }
  .card--front .wordmark__name { font-size: 32px; }

  /* service list */
  .services {
    position: absolute; left: 36px; right: 36px; top: 262px;
    list-style: none;
    display: flex; flex-wrap: wrap; justify-content: flex-end;
    column-gap: 14px; row-gap: 14px;
    font-size: 18px; color: var(--ink-white);
  }
  .services__item { display: flex; align-items: center; gap: 7px; white-space: nowrap; }
  .services__item::before {
    content: ""; width: 7px; height: 7px; border-radius: 50%;
    background: var(--accent-deep);
  }
  .services__break { flex-basis: 100%; height: 0; }

  /* front */
  .launch-art {
    position: absolute; left: 0; top: 0; width: 330px; height: 400px;
    background: linear-gradient(90deg, var(--accent-red), var(--accent-orange));
  }
  .person { position: absolute; left: 400px; top: 180px; }
  .person__name {
    font-weight: 700; font-size: 30px; letter-spacing: 0.5px;
    color: var(--accent-orange); text-transform: uppercase; white-space: nowrap;
  }
  .person__title { font-size: 20px; color: var(--ink-muted); margin-top: 4px; }
  .contact {
    position: absolute; left: 400px; top: 268px;
    list-style: none; display: flex; flex-direction: column; gap: 14px;
    font-size: 19px; color: var(--ink-muted);
  }
  .contact__row { display: flex; align-items: center; gap: 12px; white-space: nowrap; }
  .contact__icon { width: 20px; height: 20px; flex: none; }
</style>
</head>
<body>
<main class="sheet">

  <section class="card card--back" aria-label="Card back">
    <div class="wordmark">
      <span class="wordmark__dot"></span>
      <span class="wordmark__name">GLINT HARBOR</span>
    </div>
    <ul class="services">
      <li class="services__item">Eyewear Sales</li>
      <li class="services__item">Admin Duties</li>
      <li class="services__item">Revenue Collection</li>
      <li class="services__item">Leadership</li>
      <li class="services__break" aria-hidden="true"></li>
      <li class="services__item">Tech Adoption</li>
      <li class="services__item">COGS Reduction</li>
      <li class="services__item">Product Sourcing</li>
      <li class="services__item">Medical Growth</li>
    </ul>
  </section>

  <section class="card card--front" aria-label="Card front">
    <div class="launch-art" role="img" aria-label="Illustration area: large rocket launching over an orange-red glow"></div>

    <div class="wordmark">
      <span class="wordmark__dot"></span>
      <span class="wordmark__name">GLINT HARBOR</span>
    </div>

    <div class="person">
      <h1 class="person__name">Dalton Vessey</h1>
      <p class="person__title">CEO</p>
    </div>

    <ul class="contact">
      <li class="contact__row">
        <svg class="contact__icon" viewBox="0 0 24 24" aria-hidden="true">
          <path fill="#ea5a2c" d="M6.6 10.8a15.1 15.1 0 0 0 6.6 6.6l2.2-2.2a1 1 0 0 1 1-.25 11.4 11.4 0 0 0 3.6.57 1 1 0 0 1 1 1V20a1 1 0 0 1-1 1A17 17 0 0 1 3 4a1 1 0 0 1 1-1h3.5a1 1 0 0 1 1 1c0 1.25.2 2.45.57 3.57a1 1 0 0 1-.25 1z"/>
        </svg>
        <span>847-302-1964</span>
      </li>
      <li class="contact__row">
        <svg class="contact__icon" viewBox="0 0 24 24" aria-hidden="true">
          <rect x="2" y="5" width="20" height="14" fill="#ea5a2c"/>
          <path d="M2 5 L12 13 L22 5" fill="none" stroke="#0b0b0b" stroke-width="1.6"/>
        </svg>
        <span>dalton@glintharbor.example</span>
      </li>
    </ul>
  </section>

</main>
</body>
</html>
```